Family Farm Business Requires Flyer for local CSA retail sales and local advertising

We need a flyer design for our small farm to help promote our CSA business. A CSA is when someone pre-pays for a summer's worth of produce, fruit, and eggs that are raised on our farm. They receive a weekly box of produce and essentially they buy a small share of the summer's bounty. We had a logo designed by someone here on sketch harbor so we would like the flyer to include the colors of the logo. The final design should reflect the different options for people the choose and then invite them to sign up to be a CSA Customer.

Target Market(s)

Busy families and moms who are limited in time to buy groceries or healthy food or produce. People who are passionate about local food and local produce.

Industry/Entity Type

Advertising

Font styles to use
Decorative
Script

Requirements
Must have
• Our logo, our farm information (website, social media, location) and contact info as well as the various options to choose from for our CSA farm share. I also included a picture of our business card so it would be good if it matched the colors/style of our card. Also the flyer will be printed on 8.5 x 11 paper and it will be double sided.

```html
<!DOCTYPE html>
<html lang="en">
<head>
<meta charset="utf-8">
<title>2015 CSA Membership Sign-Up – Nine Hollow Farm</title>
<link href="https://fonts.googleapis.com/css2?family=Roboto+Condensed:wght@400;700&display=swap" rel="stylesheet">
<style>
:root{
  --wood-dark:#2a1a12;
  --wood-mid:#4a3226;
  --wood-light:#5e4334;
  --text:#ffffff;
  --text-soft:#e8e8e8;
  --field:#e9e9e9;
  --field-text:#1e1e1e;
  --farm-green:#1f9a4b;
  --band:rgba(15,10,8,.72);
}
*{margin:0;padding:0;box-sizing:border-box}
html,body{width:927px;height:1200px;overflow:hidden;background:var(--wood-dark)}
.flyer{position:relative;width:927px;height:1200px;overflow:hidden;font-family:"Roboto Condensed",Arial,sans-serif;color:var(--text)}
.wood-backdrop{position:absolute;inset:0;
  background:
   repeating-linear-gradient(90deg,rgba(0,0,0,.18) 0 3px,transparent 3px 150px),
   linear-gradient(180deg,var(--wood-light) 0%,var(--wood-mid) 45%,var(--wood-dark) 100%)}
.produce-photo{position:absolute;left:0;right:0;top:690px;bottom:0;
  background:
   radial-gradient(ellipse 140px 120px at 90px 140px,rgba(232,200,70,.85),transparent 70%),
   radial-gradient(ellipse 120px 110px at 230px 110px,rgba(90,30,40,.9),transparent 70%),
   radial-gradient(ellipse 130px 120px at 460px 100px,rgba(210,45,30,.9),transparent 70%),
   radial-gradient(ellipse 90px 130px at 600px 90px,rgba(240,170,40,.85),transparent 70%),
   radial-gradient(ellipse 230px 260px at 800px 60px,rgba(190,40,70,.85),transparent 70%),
   radial-gradient(ellipse 300px 200px at 330px 330px,rgba(180,35,25,.8),transparent 70%),
   linear-gradient(180deg,transparent 0%,rgba(40,60,30,.5) 60%,rgba(30,20,15,.8) 100%)}
.title{position:absolute;left:72px;top:40px;font-size:35px;font-weight:700;letter-spacing:.2px}
.member-form{position:absolute;left:74px;top:100px;width:504px}
.form-row{display:flex;gap:6px;height:23px;margin-bottom:6.3px}
.form-label{width:160px;background:var(--field);color:var(--field-text);font-size:19px;line-height:23px;padding-left:4px;white-space:nowrap}
.form-field{flex:1;background:var(--field)}
.farm-name{position:absolute;left:686px;top:90px;width:175px;text-align:center;color:var(--farm-green);font-weight:700;font-size:40px;line-height:44px;letter-spacing:3px}
.farm-name small{display:block;font-size:17px;letter-spacing:1px;line-height:30px}
.section{position:absolute;left:74px}
.section h2{font-size:19.5px;font-weight:700;margin-bottom:2px}
.section p{font-size:19px}
.section ul{list-style:none;margin-left:52px;font-size:16.5px;line-height:21.5px}
.section li::before{content:"• "}
.options{top:322px}
.payment{top:500px}
.pickup{top:609px}
.info-band{position:absolute;left:0;right:0;top:924px;bottom:0;background:var(--band)}
.mail-to{position:absolute;left:74px;top:937px;font-size:19px;line-height:26px;font-style:normal}
.mail-to h2{font-size:19.5px;font-weight:700;line-height:24px}
.responsibilities{position:absolute;left:567px;top:930px;width:338px;font-size:8.6px;line-height:10.9px;color:var(--text-soft)}
.contact-row{position:absolute;top:1113px;display:flex;align-items:center;gap:16px;font-size:17px}
.contact-row .dot{width:44px;height:44px;border-radius:50%;background:#fff;color:#222;font-size:12px;font-weight:700;display:flex;align-items:center;justify-content:center}
.social-one{left:72px}
.website{left:341px}
.social-two{left:688px}
</style>
</head>
<body>
<div class="flyer">
  <div class="wood-backdrop" role="img" aria-label="Dark weathered wooden plank background"></div>
  <div class="produce-photo" role="img" aria-label="Fresh produce: lemons, red onions, tomatoes, radishes and dill"></div>

  <h1 class="title">2015 CSA Membership Sign –Up</h1>

  <div class="member-form">
    <div class="form-row"><span class="form-label">Name</span><span class="form-field"></span></div>
    <div class="form-row"><span class="form-label">Address</span><span class="form-field"></span></div>
    <div class="form-row"><span class="form-label">State</span><span class="form-field"></span></div>
    <div class="form-row"><span class="form-label">ZIP Code</span><span class="form-field"></span></div>
    <div class="form-row"><span class="form-label">Telephone (home)</span><span class="form-field"></span></div>
    <div class="form-row"><span class="form-label">Telephone (cell)</span><span class="form-field"></span></div>
    <div class="form-row"><span class="form-label">E-male</span><span class="form-field"></span></div>
  </div>

  <div class="farm-name">NINE<br>HOLLOW<br>FARM<small>MAPLE FORK, VA</small></div>

  <section class="section options">
    <h2>Options: (Please Check)</h2>
    <p>Summer CSA (18 weeks – weekly delivery starting June 1st through October 11th)</p>
    <ul>
      <li>Mini Share (1 to 2 people) $325.00</li>
      <li>Standard Share ( 4 to 6 people) $425.00</li>
      <li>Family Share $500.00 (6 to 8 people)</li>
      <li>Fruit Share Add-on $50 to $75 depending on size (please indicate when ordering)</li>
      <li>Egg Share Add-on $90</li>
    </ul>
  </section>

  <section class="section payment">
    <h2>Payment Options</h2>
    <ul>
      <li>Check made payable to: Daniel Whitcombe / Nine Hollow Farm</li>
      <li>Debit/Credit Card/Furrowpay paid on website (coming soon!)</li>
      <li>Money Order (Daniel Whitcombe / Nine Hollow Farm)</li>
    </ul>
  </section>

  <section class="section pickup">
    <h2>Preferred Pick Up Location for Summer CSA</h2>
    <ul>
      <li>At Nine Hollow Farm on Thursdays (1820 Orchard Hill Road Maple Fork, VA 24099)</li>
      <li>Cedar County Farmers Market on Saturdays (Circle One: Pre-Picked Market Shopper)</li>
      <li>Grace Hill Chapel Eastbrook on Thursday Afternoons</li>
    </ul>
  </section>

  <div class="info-band"></div>

  <address class="mail-to">
    <h2>Please send to Completed Form and Check to:</h2>
    Nine Hollow Farm<br>
    Daniel &amp; Marla Jean Whitcombe<br>
    1820 Orchard Hill Road<br>
    Maple Fork, VA 24099<br>
    (555) 014-2286
  </address>

  <p class="responsibilities">*CSA Member Responsibilities* - Please Read<br>
  As a CSA member, you share in the bounty as well as the potential risks that may occur on the farm. Being a member enables you to form a relationship with the farmer, the farm and the people that are involved with growing the crops. Becoming a member is a commitment. We ask that if you can't finish the season as members, then you are welcome to reassign you share to another family, but we cannot issue refunds. If you are unable to pick up your box on delivery day, you must make alternate arrangements for your produce ahead of time. You can have someone else pick up your box, ask the farm not to make your box that week, or ask your site coordinator to hold the box for a later pick-up. If you forget to pick up your share, it will be donated to a food pantry or a neighborhood family. READ ANY EMAILS THAT WE SEND OUT TO YOU! This is how we communicate with you with announcements, recipes, events and special offers!</p>

  <div class="contact-row social-one"><span class="dot"></span>ninehollowfarm</div>
  <div class="contact-row website"><span class="dot">www</span>www.ninehollowfarm.com</div>
  <div class="contact-row social-two"><span class="dot"></span>ninehollowfarm</div>
</div>
</body>
</html>
```